Professional Trustee Company - Business Cards
Thornwick Crest Fiduciary Services, Inc.
Designers:
(1) Please be sure that the logo is large enough to be easily read as in some cases it appears like the words are too small to read.
(2) Please have the back of the card read: Earning your trust is our business.
RT/KPH/WN Team
Please note that I am also looking for stationary and envelope designs in black and white only. Thank you!

```html
<!DOCTYPE html>
<html lang="en">
<head>
<meta charset="utf-8">
<title>Thornwick Crest Fiduciary Services – Business Cards</title>
<link href="https://fonts.googleapis.com/css2?family=Open+Sans:wght@300;400;600&display=swap" rel="stylesheet">
<style>
  :root {
    --page: #d9d6d2;
    --card-white: #ffffff;
    --card-fade: #d4d4d4;
    --ink: #4a4a4a;
    --ink-soft: #6d6d6d;
    --rule: #9a9a9a;
    --band: #111111;
    --back: #141414;
    --back-mark: #262626;
    --light: #f2f2f2;
  }
  * { box-sizing: border-box; margin: 0; padding: 0; }
  html, body { width: 1200px; height: 995px; overflow: hidden; }
  body {
    background: var(--page);
    font-family: "Open Sans", Arial, sans-serif;
    color: var(--ink);
    position: relative;
  }
  .card {
    position: absolute;
    left: 250px;
    width: 700px;
    height: 400px;
    border-radius: 18px;
    overflow: hidden;
    box-shadow: 0 10px 28px rgba(0,0,0,.25);
  }
  /* Front */
  .card-front {
    top: 70px;
    background: linear-gradient(180deg, var(--card-white) 0%, var(--card-white) 62%, var(--card-fade) 100%);
  }
  .brand {
    position: absolute;
    left: 50px;
    top: 120px;
    width: 290px;
    display: flex;
    align-items: center;
    gap: 16px;
  }
  .brand-dot {
    flex: none;
    width: 46px; height: 46px;
    border-radius: 50%;
    background: var(--ink-soft);
  }
  .brand-name {
    font-weight: 400;
    font-size: 25px;
    line-height: 1.2;
    letter-spacing: 1px;
    color: var(--ink);
  }
  .divider {
    position: absolute;
    left: 360px;
    top: 36px;
    width: 1px;
    height: 250px;
    background: var(--rule);
  }
  .contact {
    position: absolute;
    left: 384px;
    top: 36px;
    font-size: 16px;
    line-height: 1.35;
    color: var(--ink);
  }
  .person { font-size: 17px; }
  .role { font-size: 13px; color: var(--ink-soft); margin-bottom: 30px; }
  .address { margin-bottom: 30px; }
  .lines { list-style: none; }
  .lines li { display: flex; align-items: center; gap: 12px; margin-bottom: 3px; }
  .lines svg { width: 16px; height: 16px; fill: var(--ink); }
  .web-band {
    position: absolute;
    left: 0; right: 0; bottom: 0;
    height: 52px;
    background: var(--band);
    color: var(--light);
    font-size: 17px;
    text-align: right;
    padding: 14px 40px 0 0;
    letter-spacing: .5px;
  }
  /* Back */
  .card-back {
    top: 525px;
    background: var(--back);
  }
  .back-mark {
    position: absolute;
    left: 200px;
    top: 70px;
    width: 300px;
    display: flex;
    align-items: center;
    justify-content: center;
    gap: 16px;
  }
  .back-mark .brand-dot { background: var(--back-mark); width: 90px; height: 90px; }
  .back-mark .brand-name { color: var(--back-mark); font-size: 30px; }
  .motto {
    position: absolute;
    left: 0; right: 0;
    bottom: 38px;
    text-align: center;
    color: var(--light);
    font-size: 17px;
    font-weight: 300;
    letter-spacing: 5px;
  }
</style>
</head>
<body>
  <section class="card card-front">
    <div class="brand">
      <span class="brand-dot"></span>
      <span class="brand-name">Thornwick Crest Fiduciary Services</span>
    </div>
    <div class="divider"></div>
    <div class="contact">
      <p class="person">Daniel Reeve Castellan, JD, TEP</p>
      <p class="role">President &amp; Founder</p>
      <p class="address">2185 Harlow Ridge Lane NE<br>Merrow Island, WA 98000</p>
      <ul class="lines">
        <li><svg viewBox="0 0 16 16" aria-hidden="true"><rect x="3" y="1" width="10" height="14" rx="2"/><rect x="5" y="3" width="6" height="8" fill="#fff"/></svg>555.201.3384</li>
        <li><svg viewBox="0 0 16 16" aria-hidden="true"><path d="M4 1l3 3-2 2c1 2 3 4 5 5l2-2 3 3-2 3C7 15 1 9 1 3z"/></svg>555.207.6619</li>
        <li><svg viewBox="0 0 16 16" aria-hidden="true"><rect x="1" y="3" width="14" height="10" rx="1"/><path d="M1 4l7 5 7-5" fill="none" stroke="#fff" stroke-width="1.4"/></svg>daniel@thornwickcrest.com</li>
      </ul>
    </div>
    <div class="web-band">www.thornwickcrest.com</div>
  </section>

  <section class="card card-back">
    <div class="back-mark">
      <span class="brand-dot"></span>
      <span class="brand-name">Thornwick Crest</span>
    </div>
    <p class="motto">Earning your trust is our business</p>
  </section>
</body>
</html>
```